Corporate consulting business needs a business card

I want a professional business card.... surprise me

Target Market(s)

Corprorate and Not for Profit firms and organisations

Industry/Entity Type

Consulting

Contact Information for Business Card

Logo
Corporate Consulting Services
On Time, On Budget, Beyond Expectation
Tobin Averley
Director
0427 31 64 92 (Larger)
tobin@ta-advisory.com.au
www.ta-advisory.com.au
include little icons beside the contact info:

- Envelope = email
- Phone = phone
- Globe = website

Font styles to use
Serif
Sans Serif

Requirements
Must have
• Professional and clean
Nice to have
• you tell me

```html
<!DOCTYPE html>
<html lang="en">
<head>
<meta charset="utf-8">
<title>Averley Consulting – Business Card</title>
<link href="https://fonts.googleapis.com/css2?family=Libre+Baskerville:wght@700&family=Open+Sans:wght@400;700&display=swap" rel="stylesheet">
<style>
  :root {
    --backdrop: #e9e5e1;
    --card: #ffffff;
    --ink: #3a2418;
    --text: #2b2b2b;
    --shadow: rgba(60, 45, 35, 0.18);
  }
  * { margin: 0; padding: 0; box-sizing: border-box; }
  html, body {
    width: 1200px;
    height: 997px;
    overflow: hidden;
    background: var(--backdrop);
  }
  .canvas {
    position: relative;
    width: 1200px;
    height: 997px;
  }
  .card {
    position: absolute;
    width: 560px;
    height: 320px;
    background: var(--card);
    box-shadow: 0 10px 28px var(--shadow);
  }
  .card--front { left: 150px; top: 150px; }
  .card--back  { left: 490px; top: 520px; }

  .brand {
    display: flex;
    flex-direction: column;
    align-items: center;
    gap: 14px;
  }
  .brand__mark {
    width: 64px;
    height: 64px;
    border: 3px solid var(--ink);
    border-radius: 50%;
  }
  .brand__name {
    font-family: "Libre Baskerville", Georgia, serif;
    font-weight: 700;
    font-size: 17px;
    letter-spacing: 0.04em;
    text-transform: uppercase;
    color: var(--ink);
    white-space: nowrap;
  }
  .card--front .brand {
    position: absolute;
    left: 0; right: 0; top: 100px;
  }
  .card--back .brand {
    position: absolute;
    right: 34px; top: 40px;
  }
  .card--back .brand__mark { width: 56px; height: 56px; }
  .card--back .brand__name { font-size: 14px; }

  .holder {
    position: absolute;
    left: 36px; top: 52px;
    font-family: "Open Sans", Arial, sans-serif;
  }
  .holder__name {
    font-size: 17px;
    font-weight: 700;
    color: var(--ink);
  }
  .holder__role {
    font-size: 11px;
    color: var(--text);
    margin-top: 2px;
  }
  .contacts {
    position: absolute;
    left: 36px; bottom: 44px;
    list-style: none;
    font-family: "Open Sans", Arial, sans-serif;
    font-size: 12px;
    color: var(--text);
  }
  .contacts li {
    display: flex;
    align-items: center;
    gap: 7px;
    line-height: 19px;
  }
  .contacts .contacts__phone { font-size: 13px; }
  .contacts svg { width: 14px; height: 14px; flex: none; }
</style>
</head>
<body>
<main class="canvas">

  <section class="card card--front" aria-label="Card front">
    <div class="brand">
      <span class="brand__mark" aria-hidden="true"></span>
      <span class="brand__name">Averley Consulting</span>
    </div>
  </section>

  <section class="card card--back" aria-label="Card back">
    <div class="holder">
      <p class="holder__name">Tobin Averley</p>
      <p class="holder__role">Director</p>
    </div>

    <div class="brand">
      <span class="brand__mark" aria-hidden="true"></span>
      <span class="brand__name">Averley Consulting</span>
    </div>

    <ul class="contacts">
      <li class="contacts__phone">
        <svg viewBox="0 0 14 14" aria-hidden="true">
          <circle cx="7" cy="7" r="7" fill="var(--ink)"/>
          <path d="M4.6 3.6l1.2 1.6-.7.8c.5 1 1.3 1.8 2.3 2.3l.8-.7 1.6 1.2-.8 1.2C6.6 9.9 4.1 7.4 3.9 4.4z" fill="#fff"/>
        </svg>
        0427 31 64 92
      </li>
      <li>
        <svg viewBox="0 0 14 14" aria-hidden="true">
          <circle cx="7" cy="7" r="7" fill="var(--ink)"/>
          <rect x="3.5" y="4.6" width="7" height="4.8" fill="none" stroke="#fff" stroke-width="0.9"/>
          <path d="M3.5 4.6L7 7.4l3.5-2.8" fill="none" stroke="#fff" stroke-width="0.9"/>
        </svg>
        tobin@ta-advisory.com.au
      </li>
      <li>
        <svg viewBox="0 0 14 14" aria-hidden="true">
          <circle cx="7" cy="7" r="7" fill="var(--ink)"/>
          <g fill="none" stroke="#fff" stroke-width="0.8">
            <circle cx="7" cy="7" r="3.6"/>
            <ellipse cx="7" cy="7" rx="1.6" ry="3.6"/>
            <path d="M3.4 7h7.2"/>
          </g>
        </svg>
        www.ta-advisory.com.au
      </li>
    </ul>
  </section>

</main>
</body>
</html>
```